Tallow Creek Biologics - Business Card Design

Business Card Brief;
We require a design for a business card template for our business “Tallow Creek Biologics”.
We are a firm that manufacture positive microbial formulations to enhance agricultural legume crops such as lucence, soy beans and faba beans. We also manufacture microbial formulations that aid in composting of waste organic waste to use as a natural fertilizer.
We are seeking a business card design that portrays a clean, professional organisation dedicated to enhancing nature and sustainable farming techniques.
Our website is www.farobiotix.com.au
Here is a link to a drawing of a soybean plant. One of our main products is used to help grow these. I offer it an an example of the type of graphic that might be used on the card, but will leave you to create your own design; https://pictavault.example/482913067/stock-illustration-leafy-sprout-on-a-plain.html
Two cards are required;
--------------------------------------------------------------------
Card #1
Owen T Radley
Executive Chairman
Mobile: 0412 558304
Email: owen@farobiotix.com.au
---------------------------------------------------------------------------
Card #2
Felix R Dunmore
Chief Financial & Operating Officer
Mobile: 0455 284679
Email felix@farobiotix.com.au

Many thanks
Felix Dunmore

Industry/Entity Type

Agriculture

Colors

Designer to choose colors to be used in the design.

Requirements
Must have
• An elegant design that demonstrates our commitment to enhancing nature.

```html
<!DOCTYPE html>
<html lang="en">
<head>
<meta charset="utf-8">
<title>Tallow Creek Biologics – Business Cards</title>
<link href="https://fonts.googleapis.com/css2?family=Roboto:wght@400;500&family=Roboto+Condensed:wght@400;700&display=swap" rel="stylesheet">
<style>
  :root {
    --backdrop: #2b2b2b;
    --card-white: #f3f3f3;
    --leaf-green: #a6d75f;
    --deep-green: #43a047;
    --text-grey: #4a4a4a;
    --divider: #c8c8c8;
    --white: #ffffff;
  }
  * { margin: 0; padding: 0; box-sizing: border-box; }
  html, body { width: 1200px; height: 960px; overflow: hidden; }
  body { background: var(--backdrop); position: relative; font-family: "Roboto", sans-serif; }

  .card { position: absolute; width: 600px; height: 343px; border-radius: 18px; overflow: hidden; }
  .card-front { left: 314px; top: 113px; background: var(--card-white); }
  .card-back { left: 311px; top: 472px; background: var(--leaf-green); }

  .brand-mark { position: absolute; display: flex; align-items: center; gap: 14px; }
  .brand-dot { width: 46px; height: 46px; border-radius: 50%; flex: none; }
  .brand-name { font-family: "Roboto", sans-serif; font-weight: 400; font-size: 31px; line-height: 35px; }

  .card-front .brand-mark { left: 160px; top: 95px; }
  .card-front .brand-dot { background: var(--leaf-green); }
  .card-front .brand-name { color: var(--deep-green); }

  .card-back .brand-mark { left: 142px; top: 113px; }
  .card-back .brand-dot { background: rgba(255,255,255,0.55); }
  .card-back .brand-name { color: var(--white); }

  .holder { position: absolute; right: 323px; top: 212px; text-align: right; font-family: "Roboto Condensed", sans-serif; }
  .holder-name { font-weight: 700; font-size: 22px; color: var(--deep-green); letter-spacing: 0.3px; line-height: 26px; }
  .holder-role { font-weight: 400; font-size: 16px; color: var(--leaf-green); letter-spacing: 0.4px; line-height: 22px; }

  .divider { position: absolute; left: 295px; top: 203px; width: 1px; height: 64px; background: var(--divider); }

  .contact-list { position: absolute; left: 311px; top: 206px; list-style: none; }
  .contact-list li { display: flex; align-items: center; gap: 8px; font-size: 15px; color: var(--text-grey); line-height: 19.5px; }
  .contact-list svg { width: 13px; height: 13px; fill: var(--deep-green); flex: none; }

  .footer-band { position: absolute; left: 0; bottom: 0; width: 600px; height: 23px; }

  .web-address { position: absolute; left: 0; right: 0; top: 282px; text-align: center; color: var(--white); font-size: 14px; letter-spacing: 5.2px; }
</style>
</head>
<body>
  <section class="card card-front">
    <div class="brand-mark">
      <span class="brand-dot"></span>
      <span class="brand-name">Tallow Creek<br>Biologics</span>
    </div>

    <div class="holder">
      <p class="holder-name">OWEN T RADLEY</p>
      <p class="holder-role">EXECUTIVE CHAIRMAN</p>
    </div>

    <div class="divider"></div>

    <ul class="contact-list">
      <li>
        <svg viewBox="0 0 13 13" aria-hidden="true"><path d="M3.5 0h6a1 1 0 0 1 1 1v11a1 1 0 0 1-1 1h-6a1 1 0 0 1-1-1V1a1 1 0 0 1 1-1zm.5 1.5v8.5h5V1.5zM6.5 10.8a.8.8 0 1 0 0 1.6.8.8 0 0 0 0-1.6z"/></svg>
        0412 558304
      </li>
      <li>
        <svg viewBox="0 0 13 13" aria-hidden="true"><path d="M0 3h13v1L6.5 8 0 4zM0 5.3l6.5 4 6.5-4V11H0z"/></svg>
        owen@farobiotix.com.au
      </li>
      <li>
        <svg viewBox="0 0 13 13" aria-hidden="true"><path d="M6.5 0a6.5 6.5 0 1 0 0 13 6.5 6.5 0 0 0 0-13zM3 3.5l2 .5 1 2-1.5 1.5.5 2.5L3.5 9 2 6.5zm5.5-2 1.5 2-1 1.5 1.5 1 1 2-1.5 2-1-2.5-2-1 .5-2z"/></svg>
        farobiotix.com.au
      </li>
    </ul>

    <svg class="footer-band" viewBox="0 0 600 23" aria-hidden="true">
      <rect x="0" y="0" width="600" height="23" fill="var(--leaf-green)"/>
      <polygon points="0,0 393,0 386,23 0,23" fill="var(--deep-green)"/>
      <polygon points="393,0 397,0 390,23 386,23" fill="var(--white)"/>
    </svg>
  </section>

  <section class="card card-back">
    <div class="brand-mark">
      <span class="brand-dot"></span>
      <span class="brand-name">Tallow Creek<br>Biologics</span>
    </div>
    <p class="web-address">www.farobiotix.com.au</p>
  </section>
</body>
</html>
```